A clean crisp business card for a Landscape Construction company. Designed to be easy to read contact/ info and also be appealing/interesting, unlike a traditional business card.

Industry/Entity Type

Landscape Construction

Contact Information for Business Card

Company name : Bramblecrest Landscape Construction, phone number: (555) 010-0162, website:Bramblecrestlandscapes.example, Email, sales@bramblecrestlandscapes.example

Requirements
Nice to have
• Luxurious finishes/ details…. Icons or emblems next to contact info
Should not have
• Clipart or general pictures

```html
<!DOCTYPE html>
<html lang="en">
<head>
<meta charset="utf-8">
<title>Bramblecrest Landscape Construction — Business Card</title>
<link rel="stylesheet" href="https://fonts.googleapis.com/css2?family=Cinzel:wght@500;600&family=Cormorant+Garamond:wght@500;600&display=swap">
<style>
  :root {
    --backdrop: #ebebeb;
    --card-white: #ffffff;
    --leaf-green: #a9cb4b;
    --brand-blue: #3d64b4;
    --ink: #1d1d1b;
    --shadow: 0 10px 30px rgba(0,0,0,.12);
  }
  * { box-sizing: border-box; margin: 0; padding: 0; }
  html, body { width: 1200px; height: 1200px; overflow: hidden; }
  body {
    background: var(--backdrop);
    display: flex;
    flex-direction: column;
    align-items: center;
    justify-content: center;
    gap: 60px;
  }
  .card {
    width: 860px;
    height: 490px;
    position: relative;
    overflow: hidden;
    box-shadow: var(--shadow);
  }

  /* Front side */
  .card-front { background: var(--card-white); }
  .front-brand {
    position: absolute;
    top: 0; left: 0; right: 0;
    height: 290px;
    display: flex;
    align-items: center;
    justify-content: center;
    gap: 18px;
  }
  .brand-dot {
    width: 46px; height: 46px;
    border-radius: 50%;
    background: var(--leaf-green);
    flex: none;
  }
  .brand-name {
    font-family: "Cinzel", serif;
    font-weight: 600;
    color: var(--brand-blue);
    font-size: 34px;
    line-height: 1.15;
    letter-spacing: .02em;
    white-space: nowrap;
  }
  .front-band {
    position: absolute;
    left: 0; right: 0; bottom: 0;
    height: 200px;
    background: var(--leaf-green);
    display: flex;
    align-items: center;
    justify-content: space-between;
    padding: 0 60px 0 50px;
  }
  .company-name {
    font-family: "Cinzel", serif;
    font-weight: 600;
    color: var(--ink);
    font-size: 36px;
    line-height: 1.02;
  }
  .contact-list { list-style: none; display: flex; flex-direction: column; gap: 14px; }
  .contact-item {
    display: flex;
    align-items: center;
    gap: 12px;
    font-family: "Cormorant Garamond", serif;
    font-weight: 600;
    font-size: 21px;
    color: var(--ink);
    white-space: nowrap;
  }
  .contact-icon {
    width: 30px; height: 30px;
    border-radius: 50%;
    background: var(--brand-blue);
    display: flex; align-items: center; justify-content: center;
    flex: none;
  }

  /* Back side */
  .card-back {
    background: var(--leaf-green);
    display: flex;
    align-items: center;
    justify-content: center;
  }
  .back-circle {
    width: 440px; height: 440px;
    border-radius: 50%;
    background: var(--card-white);
    display: flex;
    align-items: center;
    justify-content: center;
    text-align: center;
    padding: 20px;
  }
  .back-circle .brand-name { font-size: 24px; }
</style>
</head>
<body>

  <section class="card card-front" aria-label="Business card front">
    <div class="front-brand">
      <span class="brand-dot"></span>
      <p class="brand-name">Bramblecrest<br>Landscape Construction</p>
    </div>
    <div class="front-band">
      <h1 class="company-name">Bramblecrest<br>Landscape<br>Construction</h1>
      <ul class="contact-list">
        <li class="contact-item">
          <span class="contact-icon">
            <svg width="16" height="16" viewBox="0 0 24 24" fill="none" stroke="#fff" stroke-width="2" stroke-linecap="round" stroke-linejoin="round"><path d="M22 16.9v3a2 2 0 0 1-2.2 2 19.8 19.8 0 0 1-8.6-3.1 19.5 19.5 0 0 1-6-6A19.8 19.8 0 0 1 2.1 4.2 2 2 0 0 1 4.1 2h3a2 2 0 0 1 2 1.7c.1.9.4 1.8.7 2.7a2 2 0 0 1-.5 2.1L8 9.8a16 16 0 0 0 6 6l1.3-1.3a2 2 0 0 1 2.1-.4c.9.3 1.8.6 2.7.7a2 2 0 0 1 1.7 2z"/></svg>
          </span>
          (555) 010-0162
        </li>
        <li class="contact-item">
          <span class="contact-icon">
            <svg width="16" height="16" viewBox="0 0 24 24" fill="none" stroke="#fff" stroke-width="1.8"><circle cx="12" cy="12" r="10"/><path d="M2 12h20M12 2a15 15 0 0 1 0 20M12 2a15 15 0 0 0 0 20"/></svg>
          </span>
          Bramblecrestlandscapes.example
        </li>
        <li class="contact-item">
          <span class="contact-icon">
            <svg width="16" height="16" viewBox="0 0 24 24" fill="none" stroke="#fff" stroke-width="1.8" stroke-linejoin="round"><rect x="2" y="5" width="20" height="14" rx="1"/><path d="M2 6l10 7 10-7"/></svg>
          </span>
          sales@bramblecrestlandscapes.example
        </li>
      </ul>
    </div>
  </section>

  <section class="card card-back" aria-label="Business card back">
    <div class="back-circle">
      <p class="brand-name">Bramblecrest<br>Landscape Construction</p>
    </div>
  </section>

</body>
</html>
```